Booklet Design needed for Brightfold Web Studio

A Little bit about us:
At Brightfold Web Studio we offer our clients the very best in their website needs without the big price tag.

We take the hassle out of setting up a website and take care of the website design, domain registration, SEO and hosting.
We know how important it is to have a Visually Appealing website, that’s why when we are designing our websites we focus on the main things like branding, content, creativity, colors, layout, ease of use, and imagery.

Design Specifics:
I currently have two booklets that I give to my clients:
one before I start designing their site as a general information booklet
and the other one I give only once I complete their site - which is about how to use my editor.

I want to jazz these two booklets up and bit with a modern and professional look, and I want both the booklets to have a similar design, I would also like it to be a similar look to my website, www.brightfoldwebstudio.com.au.

Previously the budget was AUD$130. Now it is AUD$260.
This reflects your creative effort for 2 booklets.

I have uploaded the two booklets, labeled Booklet 1 (7 pages) and Booklet 2 (15 pages), inside you will find the information and images I want on each page.
The booklets also need a title page.

Thanks Designers. Will appreciate all your creative effort!

Hi Designers . i have updated the content for one of the booklets. the new file which i will upload shortly is called "New Client information Booklet content update". please use this for one of the booklets to be designed. the other booklet still needs to be done (the one with the editor information inside)Cheers Added Thursday, October 29, 2015

Target Market(s)

Small to medium Businesses

Font styles to use
Sans Serif

Colors
3176b5
5c5c5c
ffffff

Requirements
Must have
• Logo, images and content from original booklets. And the Seperate booklets for the two different booklets. Similar modern, professional design.
Nice to have
• Moder, professional design, similar look to my website. Www.brightfoldwebstudio.com.au

```html
<!DOCTYPE html>
<html lang="en">
<head>
<meta charset="utf-8">
<title>Brightfold Web Studio – Client Information Booklet</title>
<link href="https://fonts.googleapis.com/css2?family=Montserrat:wght@600;700&family=Questrial&display=swap" rel="stylesheet">
<style>
  :root {
    --bg: #e9e9e9;
    --paper: #ffffff;
    --paper-shade: #f2f2f2;
    --brand-blue: #1e9fdc;
    --brand-grey: #6a6a6a;
    --ink-white: #ffffff;
    --image-light: #e4e9ee;
    --image-dark: #c9d0d7;
  }
  * { box-sizing: border-box; margin: 0; padding: 0; }
  html, body { width: 1200px; height: 880px; overflow: hidden; }
  body {
    background: var(--bg);
    font-family: "Questrial", "Helvetica Neue", Arial, sans-serif;
    color: var(--brand-blue);
    position: relative;
  }
  .spread {
    position: absolute; left: 50px; top: 160px;
    width: 1100px; height: 560px;
    display: flex;
    box-shadow: 0 18px 30px rgba(0,0,0,0.15);
  }
  .page { position: relative; width: 550px; height: 560px; background: var(--paper); }
  .page--left { background: linear-gradient(90deg, var(--paper) 0, var(--paper) 90%, var(--paper-shade) 100%); }
  .page--right { background: linear-gradient(90deg, var(--paper-shade) 0, var(--paper) 8%); }

  .col { position: absolute; top: 0; height: 100%; }
  p, li { font-size: 8px; line-height: 1.38; }
  p + p, ul + p { margin-top: 8px; }
  ul { list-style: none; margin-top: 2px; }
  li { position: relative; padding-left: 10px; }
  li::before { content: ""; position: absolute; left: 0; top: 2px; width: 5px; height: 5px; background: currentColor; }

  .heading-display {
    font-family: "Montserrat", Arial, sans-serif; font-weight: 700;
    font-size: 14px; letter-spacing: 3px; margin-bottom: 12px;
  }
  .heading-section {
    font-weight: 400;
    font-size: 12px; line-height: 1.1; letter-spacing: 0.5px; text-transform: uppercase;
    border-bottom: 1px solid currentColor; padding-bottom: 3px; margin-bottom: 6px;
  }

  /* welcome column */
  .welcome { left: 0; width: 255px; padding: 36px 18px 0 26px; }
  .device-showcase {
    position: absolute; left: 24px; bottom: 100px; width: 130px; height: 80px;
    background: linear-gradient(135deg, var(--image-light), var(--image-dark));
  }

  /* blue panel */
  .info-panel { left: 255px; width: 295px; background: var(--brand-blue); color: var(--ink-white); padding: 32px 16px 0 20px; }
  .info-panel .duo { display: flex; gap: 14px; }
  .info-panel .duo > div { flex: 1; }
  .info-panel .choice { margin-top: 22px; }
  .info-panel .choice .heading-section { font-size: 13px; }

  /* right page */
  .feature-banner {
    position: absolute; left: 0; top: 0; width: 255px; height: 152px;
    background: var(--brand-grey); color: var(--ink-white); padding: 68px 18px 0 24px;
  }
  .feature-banner h2 { font-family: "Montserrat", Arial, sans-serif; font-weight: 700; font-size: 13px; line-height: 1.15; letter-spacing: 0.5px; }
  .feature-banner p { font-size: 10.5px; line-height: 1.25; margin-top: 8px; }
  .responsive { left: 0; top: 170px; width: 255px; padding: 0 14px 0 24px; height: auto; }
  .personal { left: 262px; width: 270px; padding: 82px 0 0 10px; }
  .personal .lead { margin-bottom: 6px; }
  .concept-image {
    position: absolute; right: 0; top: 2px; width: 115px; height: 66px;
    background: linear-gradient(135deg, var(--image-light) 0, var(--image-light) 55%, #3a3a3a 100%);
  }
</style>
</head>
<body>
  <main class="spread">
    <section class="page page--left">
      <div class="col welcome">
        <h1 class="heading-display">WELCOME</h1>
        <p>Welcome and thanks for choosing Brightfold Web Studio, part of the Northgate Solutions Group in Tarrowdale.</p>
        <p>In this information booklet you will find information about the design process, our design and editing platform, Pricing and our hosting and domain service.</p>
        <p>Your standard, successful website is made from a blend of beautiful design, clearly written content and a well-thought-out conversion funnel. And all of that's great, but who wants to just be 'standard,' when you can be so much more? To maximize your website's potential as a customer-conversion machine, you need to create a visitor experience that is highly engaging and speaks directly to your potential customers' needs.</p>
        <p>We deliver professional, high-quality websites for our clients that evoke emotion and improve interaction. Simply put, our design work delivers real, measurable results.</p>
        <p>Our state-of-the-art features are proven to increase search engine ranking, boost sales, and deliver a better overall experience across every device type.</p>
        <div class="device-showcase" role="img" aria-label="Website shown on a desktop monitor and a phone"></div>
      </div>

      <div class="col info-panel">
        <div class="duo">
          <div>
            <h2 class="heading-section">Our Aim</h2>
            <p>We take the hassle out of setting up a website and take care of the website design, domain registration, SEO and hosting. We aim:</p>
            <ul>
              <li>To design a website that the client will love.</li>
              <li>To listen to our Clients and ensure that they get the website they want and have it looking exactly how they wish.</li>
              <li>To produce smart looking, visually appealing, high quality website at an affordable price, for your Clients Businesses.</li>
              <li>To produce website without the big price tag.</li>
            </ul>
          </div>
          <div>
            <h2 class="heading-section">We Will</h2>
            <p>We will collaborate on website projects with our clients and cultivate a friendly working relationship by:</p>
            <ul>
              <li>Listen to your needs.</li>
              <li>Value your input.</li>
              <li>Being committed to developing a website that is tailored to your needs.</li>
              <li>Being prompt, reliable &amp; honest.</li>
            </ul>
            <p style="margin-top:2px">We know how important it is to have a Visually Appealing website, that's why when we are designing our website's we focus on the main things like branding, content, creativity, colors, layout, ease of use, and imagery.</p>
          </div>
        </div>
        <div class="choice">
          <h2 class="heading-section">Why we are<br>your number one choice</h2>
          <p>Because we don't have contracts or ongoing fees.</p>
          <p>We only charge a one off website design and setup fee, additional fees that will be charged is a website hosting &amp; domain registration fee (charged every one or two years), general maintenance fee if required or if you would like extra features added to your site.</p>
          <p>Once you pay for your site it's all yours! We don't hold copyright or royalties over any content on your website. Clients will also receive a package that includes how to operate the editing platform, with statistics upon how well their new website is going, and premium support.</p>
        </div>
      </div>
    </section>

    <section class="page page--right">
      <div class="feature-banner">
        <h2>BUSINESS-DRIVING<br>FEATURES</h2>
        <p>Building a beautiful website is only half the battle—you also need a website that can perform.</p>
      </div>

      <div class="col responsive">
        <h2 class="heading-section">One website that works on desktop, tablet and mobile</h2>
        <p>Traditional desktop-only sites simply won't cut it anymore. One study from MetricLane found that 49 percent of digital media time is spent on mobile devices, with tablets accounting for an additional 12 percent. With just 31 percent of time left over for desktop devices, it becomes clear that websites should be built mobile-friendly, tablet-friendly, and desktop-friendly. That's why we employ what's called responsive web design.</p>
        <p>Traditionally, responsive design means stretching and shrinking your site to fit different screen sizes. However, we take it a step further by tailoring different features for different devices as well. For example, a Click-to-Call button will appear on a mobile device, but not a tablet or desktop. The experience and the needs of a visitor can greatly differ between a mobile and desktop device, and we make sure that our content and designs consistently reflect that.</p>
      </div>

      <div class="col personal">
        <div class="concept-image" role="img" aria-label="Hand holding a glass sphere of internet keywords"></div>
        <h2 class="heading-section">Website<br>Personalization</h2>
        <p>Normally, the web is a uniform experience—every visitor gets the same experience on a website as the next guy. But over the past few years, large enterprises like Shopwell have used a strategy of website personalization to boost their conversion rate. This is because creating a one-to-one visitor experience speaks directly to a potential customer and their needs.</p>
        <p>However, we don't think this technology should be reserved for companies with vast budgets and endless resources. So, we've developed a way to offer this kind advanced customer-conversion technology to small business owners like you.</p>
        <p class="lead">Stats on Website Personalization:</p>
        <p>There's a few statistics that show how much web personalization can help the success of your website.</p>
        <ul>
          <li>Nearly three in four (74 percent) online consumers get frustrated with websites when the content that's displayed, such as offers or promotions, has nothing to do with their interests.</li>
          <li>In-house marketers who personalize their customers' web experiences see an average of 19 percent uplift in sales.</li>
        </ul>
        <p>Our agency can create a dynamic website that changes based off user's behavior such as visit history, proximity to your business, time of day/week/month, device type, etc., that adapts its content to deliver a tailored experience with business-driving features that increase conversions.</p>
        <p>Website personalization truly is the next great frontier in web design.</p>
      </div>
    </section>
  </main>
</body>
</html>
```